Do me a Simple layout and Blow the stockings off my clients!!

I am a Personal Stylist focusing on helping women/mothers needing to revamp their wardrobe and feel confident and fresh again. I'm receiving very positive feedback and growing interest in the services I offer. I provide a 'Client Profile' as part of that service in a word document (saved as PDF). What I'm needing is to turn the average looking word document into a modern, funky and professional document template. I have a business logo and copy.
The template should be fluid, easy to update and communicate sassy, funky and professional.

Target Market(s)

Females 25-65.

Industry/Entity Type

Business

Font styles to use
Other font styles liked:
• HelveticaNeue Condensed, or Raleway

Requirements
Must have
• Colours and styles consistent with logo, and fashion industry.
• Interesting and emotive elements around the content.
• Create clear 'sections' with high impact (full coloured page with single, simple section heading ?)
Nice to have
• Ability to feature 'subjects' photos in interesting ways through out the document.
• Don't just stick with portrait layout, landscape is fine too.
Should not have
• Not too busy - less is more.

```html
<!DOCTYPE html>
<html lang="en">
<head>
<meta charset="utf-8">
<title>Client Profile – Lena Marlowe Personal Shopping</title>
<link rel="stylesheet" href="https://fonts.googleapis.com/css2?family=Raleway:wght@100;200;300;400;500&family=Dancing+Script:wght@400&family=Open+Sans:wght@400;700&display=swap">
<style>
  :root {
    --canvas: #ffffff;
    --paper: #ededed;
    --hair-grey: #c9caca;
    --magenta: #d62a8c;
    --ink: #1a1a1a;
    --muted: #6b6b6b;
    --card: #ffffff;
    --on-magenta: #ffffff;
  }
  * { margin: 0; padding: 0; box-sizing: border-box; }
  html, body { width: 1200px; height: 900px; overflow: hidden; background: var(--canvas); }
  .spread { position: relative; width: 1200px; height: 900px; }

  .page { position: absolute; top: 110px; width: 520px; height: 737px; background: var(--paper); overflow: hidden; }
  .page--cover { left: 72px; }
  .page--profile { left: 633px; }

  .bands { position: absolute; inset: 0; }

  .brand { position: absolute; font-family: "Raleway", sans-serif; }
  .brand__name { font-weight: 400; color: var(--magenta); font-size: 25px; line-height: 1.05; letter-spacing: .5px; }
  .brand__owner { font-size: 8px; letter-spacing: 1px; color: var(--muted); margin-top: 5px; text-align: right; }
  .page--cover .brand { left: 32px; top: 52px; width: 150px; }
  .page--profile .brand { left: 392px; top: 640px; width: 120px; }
  .page--profile .brand__name { font-size: 21px; }

  .cover-art {
    position: absolute; left: 118px; top: 78px; width: 402px; height: 659px;
    background: radial-gradient(ellipse at 45% 35%, var(--hair-grey) 0%, #d6d6d6 45%, var(--paper) 75%);
  }

  .title { font-weight: normal; }
  .title__main, .title__script {
    position: absolute; white-space: nowrap; line-height: 1; transform-origin: left bottom;
  }
  .title__main { font-family: "Raleway", sans-serif; font-weight: 100; color: var(--ink); }
  .title__script { font-family: "Dancing Script", cursive; color: var(--magenta); }

  .page--cover .title__main { left: 18px; top: 518px; font-size: 74px; letter-spacing: -1px; transform: rotate(-11deg); }
  .page--cover .title__script { left: 212px; top: 568px; font-size: 52px; transform: rotate(-34deg); }

  .cover-credit { font-family: "Raleway", sans-serif; font-weight: 300; }
  .cover-credit__name, .cover-credit__service {
    position: absolute; white-space: nowrap; line-height: 1; font-size: 20px; letter-spacing: .3px; transform-origin: left bottom;
  }
  .cover-credit__name { left: 48px; top: 627px; color: var(--ink); transform: rotate(-6deg); }
  .cover-credit__service { left: 54px; top: 685px; color: var(--magenta); transform: rotate(-14deg); }

  .profile-art { position: absolute; inset: 0; background: linear-gradient(180deg, var(--paper) 0%, #e6e6e6 50%, var(--paper) 100%); }

  .page--profile .title__main { left: 12px; top: 84px; font-size: 46px; color: var(--on-magenta); transform: rotate(-17deg); }
  .page--profile .title__script { left: 146px; top: 89px; font-size: 30px; color: var(--on-magenta); transform: rotate(-40deg); }

  .profile-card {
    position: absolute; left: 109px; top: 157px; width: 316px; height: 470px;
    background: var(--card); box-shadow: 0 4px 14px rgba(0,0,0,.35);
    padding: 21px 16px 0 16px; font-family: "Open Sans", sans-serif; font-size: 9.6px; line-height: 13.6px; color: var(--ink);
  }
  .profile-card__row { margin-bottom: 13px; }
  .profile-card__label { font-weight: 700; font-size: 11px; }
  .checklist { list-style: none; }
  .checklist li::before { content: "\2714"; font-size: 7px; margin: 0 4px 0 4px; }
  .profile-card__celebs { padding-left: 1px; }
</style>
</head>
<body>
<main class="spread">

  <section class="page page--cover">
    <div class="cover-art" role="img" aria-label="Illustration of a stylish woman with a grey bob haircut, sunglasses and pink lips"></div>
    <svg class="bands" width="520" height="737" viewBox="0 0 520 737" aria-hidden="true">
      <polygon points="0,310 520,152 520,230 0,392" fill="var(--magenta)" opacity="0.95"/>
      <polygon points="461,370 520,402 520,510 404,475" fill="var(--magenta)"/>
    </svg>
    <div class="brand">
      <div class="brand__name">Totes &amp; Tulle</div>
      <div class="brand__owner">LENA MARLOWE</div>
    </div>
    <h1 class="title">
      <span class="title__main">CLIENT</span>
      <span class="title__script">profile</span>
    </h1>
    <div class="cover-credit">
      <p class="cover-credit__name">LENA MARLOWE</p>
      <p class="cover-credit__service">PERSONAL SHOPPING</p>
    </div>
  </section>

  <section class="page page--profile">
    <div class="profile-art" role="img" aria-label="Faint line drawings of clothing, shoes, handbags and accessories"></div>
    <svg class="bands" width="520" height="737" viewBox="0 0 520 737" aria-hidden="true">
      <polygon points="0,88 247,12 262,86 0,170" fill="var(--magenta)"/>
    </svg>
    <h2 class="title">
      <span class="title__main">CLIENT</span>
      <span class="title__script">profile</span>
    </h2>

    <article class="profile-card">
      <p class="profile-card__row"><span class="profile-card__label">Client:</span> Jo</p>
      <p class="profile-card__row"><span class="profile-card__label">Body Shape:</span> The Brick, shorter waist.</p>
      <div class="profile-card__row">
        <p class="profile-card__label">Main characteristics:</p>
        <ul class="checklist">
          <li>Broad shoulders</li>
          <li>Hips inline with shoulders</li>
          <li>No shapely waist line</li>
          <li>Possibly larger (ish) thighs</li>
        </ul>
      </div>
      <div class="profile-card__row">
        <p class="profile-card__label">Main goals in dressing ‘The Brick’:</p>
        <ul class="checklist">
          <li>Create curves using shapely, flowing pieces</li>
          <li>Look for curved edges on garments</li>
          <li>Sweetheart necklines will instantly create a more shapely start to your upper body</li>
          <li>Use patterns to accentuate your best areas and detract from others.</li>
          <li>Use stripes of varying sizes, to create a shapely illusion</li>
          <li>For accessories look for curvy jewelry and handbags</li>
        </ul>
      </div>
      <div class="profile-card__row">
        <p class="profile-card__label">Styles to avoid:</p>
        <ul class="checklist">
          <li>Square cut or boxed edge jackets</li>
          <li>Short skirts (mini) or shorts which will cut you off mid thigh</li>
          <li>Box pleats or pleats at the front of trousers</li>
          <li>Look for shoes that add to the flow of your garment, nothing too solid, or chunky</li>
        </ul>
      </div>
      <p class="profile-card__celebs"><span class="profile-card__label">Celebrity ‘Bricks’:</span> Ava Lindqvist, Mira Castell, Dana Whitford</p>
    </article>

    <div class="brand">
      <div class="brand__name">Totes &amp; Tulle</div>
      <div class="brand__owner">LENA MARLOWE</div>
    </div>
  </section>

</main>
</body>
</html>
```